RoveKin
Quilly: I really like what you've come up with so far especially with #4 and the greyed out luggage. I would like you to check out my website to see if anything inspires you.
www.rovekin-example.com
Great work!!!

```html
<!DOCTYPE html>
<html lang="en">
<head>
<meta charset="utf-8">
<title>RoveKin business card</title>
<link href="https://fonts.googleapis.com/css2?family=Open+Sans:wght@400;600;700;800&display=swap" rel="stylesheet">
<style>
  :root {
    --stage: #2a2a2a;
    --card: #ffffff;
    --accent: #1aa6dc;
    --ink: #1b1b1b;
    --muted: #444444;
  }
  html, body {
    margin: 0;
    padding: 0;
    width: 1200px;
    height: 871px;
    overflow: hidden;
    background: var(--stage);
    font-family: "Open Sans", Arial, sans-serif;
  }
  .canvas {
    position: relative;
    width: 1200px;
    height: 871px;
  }
  .card {
    position: absolute;
    background: var(--card);
    border-radius: 28px;
    overflow: hidden;
  }
  .card-front {
    left: 72px;
    top: 65px;
    width: 641px;
    height: 398px;
  }
  .card-back {
    left: 468px;
    top: 494px;
    width: 648px;
    height: 338px;
  }
  .band {
    position: absolute;
    top: 130px;
    height: 130px;
    background: var(--accent);
  }
  .band-left { left: 0; width: 34px; }
  .band-right { right: 0; width: 18px; }
  .brand {
    position: absolute;
    display: flex;
    align-items: center;
    gap: 14px;
    font-weight: 800;
    color: var(--ink);
    letter-spacing: -0.5px;
  }
  .brand-mark {
    border-radius: 50%;
    background: var(--accent);
    flex: none;
  }
  .card-front .brand {
    left: 48px;
    top: 160px;
    font-size: 56px;
  }
  .card-front .brand-mark { width: 40px; height: 40px; }
  .card-back .brand {
    left: 50%;
    top: 168px;
    transform: translateX(-50%);
    font-size: 40px;
  }
  .card-back .brand-mark { width: 28px; height: 28px; }
  .holder {
    position: absolute;
    left: 362px;
    top: 60px;
  }
  .holder-name {
    margin: 0;
    font-size: 25px;
    font-weight: 600;
    color: var(--accent);
  }
  .holder-title {
    margin: 4px 0 0;
    font-size: 15px;
    color: var(--muted);
  }
  .contact {
    position: absolute;
    left: 362px;
    top: 272px;
    margin: 0;
    padding: 0;
    list-style: none;
    font-size: 13px;
    line-height: 19.5px;
    color: var(--muted);
  }
  .contact .gap { margin-top: 8px; }
  .contact .label { color: var(--accent); }
  .contact .label-plain { color: var(--muted); }
  .back-web {
    position: absolute;
    left: 0;
    right: 0;
    top: 284px;
    text-align: center;
    font-size: 14px;
    letter-spacing: 7px;
    color: var(--muted);
  }
</style>
</head>
<body>
<main class="canvas">
  <section class="card card-front" aria-label="Business card front">
    <div class="band band-left"></div>
    <div class="band band-right"></div>
    <div class="brand"><span class="brand-mark"></span>RoveKin</div>
    <div class="holder">
      <h1 class="holder-name">Daniel K. Marlowe</h1>
      <p class="holder-title">Executive Director</p>
    </div>
    <ul class="contact">
      <li>4210 Ledger Ln</li>
      <li>Fairview Hills, CO. 80000</li>
      <li class="gap"><span class="label">Toll free :</span> 1-888-ROVE-KN (1-888-555-0148)</li>
      <li><span class="label">Cell :</span> 555-013-2290</li>
      <li><span class="label">Email :</span> dmarlowe@rovekin-example.com</li>
      <li><span class="label-plain">Web :</span> www.rovekin-example.com</li>
    </ul>
  </section>

  <section class="card card-back" aria-label="Business card back">
    <div class="brand"><span class="brand-mark"></span>RoveKin</div>
    <p class="back-web">www.rovekin-example.com</p>
  </section>
</main>
</body>
</html>
```